Marbury Church Winter Cantata 2013

Create a 18x22 inch poster for an upcoming church concert event with the following details:
Theme: Jesus Is Coming Again
Date:12/21/13 Time: 10:40am
Featuring the Choirs of the Marbury Church and special guests.
Marbury FBC Church
514-36 92nd Street,
Laurelton, NY 11287
Pastor Delton K. Fairweather
The target audience is predominantly african-american
The concert theme has been changed to: "Jesus The Light of the World"
Church

```html
<!DOCTYPE html>
<html lang="en">
<head>
<meta charset="utf-8">
<title>Marbury Church Winter Cantata 2013</title>
<link rel="stylesheet" href="https://fonts.googleapis.com/css2?family=Tinos:wght@400;700&family=Zilla+Slab:wght@700&family=Tangerine:wght@700&display=swap">
<style>
  :root {
    --sky-gold: #f6b73a;
    --warm-orange: #ea8131;
    --deep-red: #c7352a;
    --royal-purple: #7b2a85;
    --dark-purple: #651d70;
    --star-white: #fff8e6;
  }
  html, body {
    margin: 0;
    padding: 0;
    width: 982px;
    height: 1200px;
    overflow: hidden;
  }
  .poster {
    position: relative;
    width: 982px;
    height: 1200px;
    overflow: hidden;
    background: linear-gradient(170deg, var(--sky-gold) 0%, var(--warm-orange) 45%, #d9582c 75%, var(--deep-red) 100%);
    font-family: "Tinos", "Times New Roman", serif;
    color: var(--royal-purple);
  }
  .music-backdrop {
    position: absolute;
    inset: 0;
    background:
      radial-gradient(ellipse 420px 520px at 200px 700px, rgba(255,220,170,0.22), transparent 70%),
      radial-gradient(ellipse 300px 400px at 820px 420px, rgba(180,90,30,0.18), transparent 70%);
  }
  .eyebrow {
    position: absolute;
    left: 60px;
    top: 44px;
    margin: 0;
    font-size: 32px;
    font-weight: 400;
    letter-spacing: 1.5px;
    transform: scaleY(0.9);
    transform-origin: left top;
  }
  .title-word {
    position: absolute;
    left: 95px;
    top: -40px;
    margin: 0;
    font-family: "Tangerine", "Brush Script MT", cursive;
    font-weight: 700;
    font-size: 470px;
    line-height: 1;
    color: var(--royal-purple);
    transform: rotate(-6deg);
    transform-origin: left top;
    white-space: nowrap;
  }
  .guiding-star {
    position: absolute;
    left: 705px;
    top: 0;
    width: 240px;
    height: 310px;
  }
  .subtitle {
    position: absolute;
    right: 72px;
    top: 298px;
    margin: 0;
    font-family: "Zilla Slab", "Rockwell", serif;
    font-weight: 700;
    font-size: 64px;
    line-height: 56px;
    letter-spacing: 2px;
    text-align: right;
    color: var(--royal-purple);
  }
  .details p {
    position: absolute;
    margin: 0;
    white-space: nowrap;
    transform: translateX(-50%);
    letter-spacing: 0.6px;
  }
  .featuring { left: 600px; top: 490px; font-size: 27px; font-weight: 700; }
  .choirs { left: 595px; top: 528px; font-size: 34px; }
  .guests { left: 594px; top: 572px; font-size: 34px; }
  .date { left: 593px; top: 617px; font-size: 35px; }
  .venue { left: 489px; top: 683px; font-size: 32px; }
  .street { left: 492px; top: 722px; font-size: 27px; letter-spacing: 1.5px; }
  .city { left: 490px; top: 754px; font-size: 27px; letter-spacing: 1.5px; }
  .pastor { left: 496px; top: 795px; font-size: 34px; }
  .nativity-scene {
    position: absolute;
    left: 150px;
    top: 845px;
    width: 690px;
    height: 330px;
  }
</style>
</head>
<body>
<main class="poster">
  <div class="music-backdrop" role="img" aria-label="Faint scattered musical notes across the warm background"></div>

  <p class="eyebrow">WINTER CANTATA</p>

  <h1 class="title-word">Jesus</h1>

  <svg class="guiding-star" role="img" aria-label="Glowing star of Bethlehem" viewBox="0 0 240 310">
    <defs>
      <radialGradient id="starGlow" cx="50%" cy="50%" r="50%">
        <stop offset="0%" stop-color="#fff8e6" stop-opacity="1"/>
        <stop offset="35%" stop-color="#fff2cc" stop-opacity="0.7"/>
        <stop offset="100%" stop-color="#fff2cc" stop-opacity="0"/>
      </radialGradient>
    </defs>
    <ellipse cx="120" cy="145" rx="120" ry="150" fill="url(#starGlow)"/>
  </svg>

  <h2 class="subtitle">THE<br>LIGHT OF<br>THE WORLD</h2>

  <section class="details">
    <p class="featuring">Featuring</p>
    <p class="choirs">The Choirs of The Marbury Church</p>
    <p class="guests">And Special Guests</p>
    <p class="date">December 21, 2013 at 10:40 a.m.</p>
    <p class="venue">Marbury Church of the Faithful Brethren</p>
    <p class="street">514-36 92nd Street</p>
    <p class="city">Laurelton, NY 11287</p>
    <p class="pastor">Delton K. Fairweather, Senior Pastor</p>
  </section>

  <svg class="nativity-scene" role="img" aria-label="Silhouette of the nativity stable with the holy family, shepherds, palm trees and animals" viewBox="0 0 690 330">
    <defs>
      <linearGradient id="sceneTone" x1="0" y1="0" x2="0" y2="1">
        <stop offset="0%" stop-color="#651d70" stop-opacity="0.55"/>
        <stop offset="100%" stop-color="#651d70" stop-opacity="0.85"/>
      </linearGradient>
    </defs>
    <rect x="0" y="0" width="690" height="330" rx="6" fill="url(#sceneTone)"/>
  </svg>
</main>
</body>
</html>
```